Best Seller Book Cover ...

Book Title: Stop Chasing Meaning: Pick a Trail, Keep to That Trail, Mind the Geese

Edgy, Minimalist, Compelling, Attractive, Classy design.

Very clean. See examples.,

Target Market(s)

Mid Life People ages 38-55 Male and Female equally

Requirements

Nice to have
• Nice to Have:

Minimalist and eye catching ( i have loaded a few examples of what this means)
Should not have
• Clip Art
Clutter

```html
<!DOCTYPE html>
<html lang="en">
<head>
<meta charset="utf-8">
<title>Stop Chasing Meaning – Book Cover</title>
<link rel="stylesheet" href="https://fonts.googleapis.com/css2?family=Open+Sans:wght@600&family=PT+Sans:wght@700&display=swap">
<style>
  :root {
    --cover-red: #e31e24;
    --ink-black: #000000;
    --paper-white: #ffffff;
    --edge-grey: #4a4a4a;
  }
  html, body {
    margin: 0;
    padding: 0;
    width: 851px;
    height: 1200px;
    overflow: hidden;
    background: var(--paper-white);
  }
  .cover {
    position: relative;
    width: 851px;
    height: 1200px;
    box-sizing: border-box;
    border: 2px solid var(--edge-grey);
    background: var(--cover-red);
    overflow: hidden;
  }
  .cover-art {
    position: absolute;
    inset: 0;
    width: 100%;
    height: 100%;
  }
  .walker,
  .start-dot {
    fill: var(--ink-black);
  }
  .title-text {
    font-family: "Open Sans", "Myriad Pro", sans-serif;
    font-weight: 600;
    font-size: 70px;
    fill: var(--ink-black);
  }
  .subtitle-band {
    position: absolute;
    left: 0;
    right: 0;
    bottom: 0;
    height: 169px;
    background: var(--ink-black);
    display: flex;
    align-items: center;
    justify-content: center;
  }
  .subtitle {
    margin: 0;
    padding-top: 6px;
    font-family: "PT Sans", "Arial Narrow", sans-serif;
    font-weight: 700;
    font-size: 41px;
    line-height: 57px;
    color: var(--paper-white);
    text-align: center;
  }
</style>
</head>
<body>
  <main class="cover">
    <svg class="cover-art" viewBox="0 0 851 1200" xmlns="http://www.w3.org/2000/svg">
      <g role="img" aria-label="Black silhouette of a man in a suit walking toward the viewer">
        <rect class="walker" x="370" y="172" width="105" height="331" rx="40"/>
      </g>
      <circle class="start-dot" cx="417" cy="539" r="16"/>
      <text class="title-text" transform="translate(418 588) rotate(45)">
        <tspan x="0" y="0">Stop Chasing</tspan>
        <tspan x="0" dy="80">Meaning:</tspan>
      </text>
    </svg>
    <footer class="subtitle-band">
      <p class="subtitle">Pick a Trail, Keep to That Trail,<br>Mind the Geese</p>
    </footer>
  </main>
</body>
</html>
```